5 Banner für die Startseite der Hompage
Zielgruppe
Wir sind eine 'kreative' kleine Truppe, die mit neuen Ideen versuchen wollen, auch mal andere Wege in den Projekten zu gehen.
unsere neue Webseite lautet
Aufgabenstellung
Auf meiner Webseite www.kavelorn.de habe ich bereits einen ersten Vorschlag eingefügt.
Es geht um die 5 Banner auf der Startseite; diese sollen sowohl Designtechnisch als auch optisch sehr ansprechend wirken, um das Interesse potentieller Kunden zu wecken.
Meine Farben habe ich mit angehängt.
Der Text könnte sich noch anpassen, muss aber mit in den Banner aufgenommen werden.
Breite sollte 1200Pixel; Höhe 600Pixel

```html
<!DOCTYPE html>
<html lang="de">
<head>
<meta charset="utf-8">
<title>Kavelorn – Startseite</title>
<link rel="stylesheet" href="https://fonts.googleapis.com/css2?family=Carlito:ital,wght@0,400;0,700;1,400&family=Lato:wght@400;700;900&display=swap">
<style>
  :root {
    --pink: #f0468d;
    --pink-soft: #f58dba;
    --ink: #3a4347;
    --ink-dark: #2b3a40;
    --page: #f7f8f8;
    --white: #ffffff;
  }
  * { margin: 0; padding: 0; box-sizing: border-box; }
  html, body { width: 1200px; height: 606px; overflow: hidden; background: var(--page); }
  body { position: relative; font-family: "Carlito", "Calibri", sans-serif; color: var(--ink); }

  .hero {
    position: absolute; left: 0; top: 0; width: 1200px; height: 481px;
    background:
      linear-gradient(180deg, rgba(120,70,70,0.55) 0%, rgba(150,100,100,0.35) 40%, rgba(110,110,140,0.45) 75%, rgba(100,105,135,0.55) 100%),
      linear-gradient(90deg, #8b5f5c 0%, #a07774 45%, #8a6a70 100%);
  }

  .site-header { position: absolute; left: 0; top: 0; width: 1200px; height: 50px; }
  .site-logo {
    position: absolute; left: 190px; top: 11px;
    font-family: "Carlito", sans-serif; font-weight: 700; font-size: 21px; color: var(--white);
  }
  .main-nav { position: absolute; left: 678px; top: 17px; display: flex; gap: 14px; }
  .main-nav a {
    font-family: "Lato", sans-serif; font-size: 9px; color: var(--white); text-decoration: none;
  }

  .slide {
    position: absolute; left: 184px; top: 80px; width: 788px; height: 361px;
    background: var(--white); overflow: hidden;
    box-shadow: 0 6px 14px rgba(0,0,0,0.35);
  }
  .slide-photo {
    position: absolute; right: 0; top: 0; width: 350px; height: 361px;
    background: linear-gradient(90deg, rgba(255,255,255,1) 0%, #eeeeee 35%, #e2e2e2 70%, #ebebeb 100%);
  }
  .slide-ring { position: absolute; left: 0; top: 0; }
  .slide-logo {
    position: absolute; left: 698px; top: 334px;
    font-weight: 700; font-size: 18px; color: var(--ink);
  }

  .quote-mark {
    position: absolute; left: 24px; top: 42px;
    font-family: "Carlito", sans-serif; font-style: italic; font-weight: 700;
    font-size: 72px; line-height: 1; color: var(--pink);
  }
  .quote {
    position: absolute; left: 68px; top: 38px; width: 420px;
    font-size: 25.5px; line-height: 33px; color: var(--ink);
  }
  .quote-close {
    font-style: italic; font-weight: 700; font-size: 40px; color: var(--pink);
    line-height: 0; position: relative; top: 6px;
  }
  .quote-author {
    font-style: italic; font-size: 13.5px; color: var(--ink); margin-left: 6px;
  }
  .slide-text {
    position: absolute; left: 71px; top: 266px; width: 470px;
    font-size: 12.2px; line-height: 16.4px; color: var(--ink);
  }
  .read-more {
    position: absolute; left: 69px; top: 310px;
    font-weight: 700; font-size: 18px; color: var(--pink); text-decoration: none;
  }

  .slide-arrow {
    position: absolute; top: 236px; width: 33px; height: 49px;
    background: var(--pink); color: var(--white);
    font-family: "Lato", sans-serif; font-weight: 900; font-size: 26px;
    display: flex; align-items: center; justify-content: center;
  }
  .slide-arrow::before {
    content: ""; position: absolute; top: -12px; width: 0; height: 0;
    border-bottom: 12px solid #9c2c5a;
  }
  .slide-arrow.prev { left: 174px; }
  .slide-arrow.prev::before { right: 0; border-left: 10px solid transparent; }
  .slide-arrow.next { left: 949px; }
  .slide-arrow.next::before { left: 0; border-right: 10px solid transparent; }

  .section-title {
    position: absolute; left: 0; top: 539px; width: 1200px; text-align: center;
    font-family: "Lato", sans-serif; font-weight: 900; font-size: 30px; color: var(--ink-dark);
    letter-spacing: 0.2px;
  }
  .section-divider { position: absolute; left: 550px; top: 590px; }
</style>
</head>
<body>
  <div class="hero" role="img" aria-label="Hintergrundfoto: Bauplan mit Linienraster in rötlich-braunen und graublauen Tönen"></div>

  <header class="site-header">
    <div class="site-logo">Kavelorn</div>
    <nav class="main-nav">
      <a href="#">Home</a>
      <a href="#">Unser Ansatz</a>
      <a href="#">Produkte</a>
      <a href="#">Dienstleistungen</a>
      <a href="#">Schulungen</a>
    </nav>
  </header>

  <section class="slide">
    <div class="slide-photo" role="img" aria-label="Foto: gerollte Baupläne und technische Zeichnung in hellem Grau"></div>
    <svg class="slide-ring" width="788" height="361" viewBox="0 0 788 361" aria-hidden="true">
      <circle cx="738" cy="330" r="109" fill="none" stroke="var(--pink-soft)" stroke-width="38" opacity="0.9"/>
    </svg>
    <div class="slide-logo">Kavelorn</div>

    <div class="quote-mark">”</div>
    <p class="quote">Wir tun nichts Außergewöhnliches, wir sind bloß erfolgreich, weil wir ganz gewöhnliche Dinge ganz außergewöhnlich tun.<span class="quote-close">”</span><span class="quote-author">Ulrich Brenner</span></p>

    <p class="slide-text">Abhängig davon, was Sie wirklich brauchen beraten wir Sie zu unseren Methoden, führen diese bei Ihnen einm begleiten Ihre Projekte oder übernehmen die komplette Porjektverantwortung.</p>
    <a class="read-more" href="#">&gt;&gt; Lesen Sie mehr</a>
  </section>

  <div class="slide-arrow prev">&lt;</div>
  <div class="slide-arrow next">&gt;</div>

  <h2 class="section-title">UNSER ANSATZ</h2>
  <svg class="section-divider" width="100" height="12" viewBox="0 0 100 12" aria-hidden="true">
    <g stroke="var(--ink-dark)" stroke-width="3" stroke-linecap="round">
      <path d="M3 2 L11 10 M11 2 L3 10"/>
      <path d="M21 2 L29 10 M29 2 L21 10"/>
      <path d="M39 2 L47 10 M47 2 L39 10"/>
    </g>
  </svg>
</body>
</html>
```